Maplerise Trading Inc. needs an innovative idea for letterhead and visiting cards.

Maplerise Trading Inc. is a Canadian brand since 2007. It is a renown dealer of kids and office furniture locally. Moreover, exporting electric fixtures e.g. switches, LED's, down-lights etc. to Middle East and Africa. We have initiated a number of steps including re-branding, to boost our export in 2020. We have successfully designed our new logo a few months ago through 'Artfolio' and now we are looking for an innovative idea for a letterhead.
Some key points:
• Red, black and white are the three colors used in all our packaging and furniture. (grey is optional)
• Shouldn’t be too wide.
• Use of watermark is preferable.
• You can visit our North American site at www.mapleriseinc.com. Export website of the company will be launched soon. www.mapleriseinc.ca
• Same letterhead will be used locally and internationally.
• Our new logo and sample packaging is attached.

```html
<!DOCTYPE html>
<html lang="en">
<head>
<meta charset="utf-8">
<title>Maplerise Trading Inc. — Letterhead &amp; Visiting Cards</title>
<link rel="stylesheet" href="https://fonts.googleapis.com/css2?family=Questrial&family=Lato:wght@400;700&display=swap">
<style>
  :root {
    --red: #a3161c;
    --charcoal: #3b3b3d;
    --ink: #3a3a3a;
    --paper: #ffffff;
    --backdrop: #e4e3e1;
    --watermark: #f0d4d5;
  }
  * { box-sizing: border-box; margin: 0; padding: 0; }
  html, body { width: 1200px; height: 800px; overflow: hidden; }
  body {
    background: var(--backdrop);
    font-family: "Questrial", "Century Gothic", sans-serif;
    color: var(--ink);
    position: relative;
  }
  .sheet, .card {
    position: absolute;
    background: var(--paper);
    box-shadow: 0 4px 14px rgba(0,0,0,.18);
    overflow: hidden;
  }
  .band { position: absolute; left: 0; width: 100%; display: block; }

  /* Letterhead */
  .letterhead { left: 160px; top: 30px; width: 572px; height: 740px; }
  .letterhead .band-top { top: 0; height: 12px; }
  .letterhead .band-bottom { bottom: 0; height: 12px; }

  .brand { position: absolute; display: flex; align-items: center; }
  .brand-square { background: var(--red); flex: none; }
  .brand-name {
    color: var(--charcoal);
    font-family: "Questrial", "Century Gothic", sans-serif;
    font-weight: 400;
    text-transform: uppercase;
    line-height: 1;
  }
  .brand-name span { display: block; }
  .letterhead .brand { left: 134px; top: 92px; gap: 16px; }
  .letterhead .brand-square { width: 20px; height: 20px; }
  .letterhead .brand-name { font-size: 36px; letter-spacing: 1px; }
  .letterhead .brand-name span + span { margin-top: 6px; }

  .letter-body {
    position: absolute; left: 50px; top: 226px; width: 452px;
    font-size: 11px; line-height: 18.7px; text-align: justify;
    color: #2e2e2e;
  }
  .letter-body p + p { margin-top: 18.7px; }

  .signature { position: absolute; right: 72px; top: 596px; text-align: right; }
  .signature .name { font-size: 15px; }
  .signature .role { font-size: 10.5px; margin-top: 10px; }

  .watermark { position: absolute; background: var(--watermark); border-radius: 50%; }
  .letterhead .watermark { left: 238px; top: 612px; width: 70px; height: 70px; }

  .contacts {
    position: absolute; left: 50px; top: 692px; width: 480px;
    display: flex; justify-content: space-between;
    font-family: "Lato", sans-serif; font-size: 10px; line-height: 13px; color: #222;
  }
  .contacts dl { display: grid; grid-template-columns: auto auto; column-gap: 4px; }
  .contacts dt { color: var(--red); font-weight: 700; font-size: 8px; }
  .contacts .address { color: var(--red); font-weight: 700; }

  /* Visiting cards */
  .card { left: 772px; width: 272px; height: 160px; }
  .card .band-bottom { bottom: 0; height: 6px; }
  .card-back { top: 80px; }
  .card-front { top: 290px; }

  .card-back .brand { left: 66px; top: 22px; gap: 8px; }
  .card-back .brand-square { width: 10px; height: 10px; }
  .card-back .brand-name { font-size: 15px; }
  .card-back .brand-name span + span { margin-top: 3px; }
  .card-back .watermark { left: 190px; top: 74px; width: 36px; height: 36px; }
  .holder { position: absolute; left: 14px; top: 100px; font-family: "Lato", sans-serif; }
  .holder .name { color: var(--red); font-weight: 700; font-size: 7.5px; }
  .holder .role { font-size: 6px; color: #555; }
  .card-contacts {
    position: absolute; left: 14px; top: 130px; width: 246px;
    display: flex; justify-content: space-between;
    font-family: "Lato", sans-serif; font-size: 4.8px; line-height: 6.5px; color: #333;
  }
  .card-contacts b { color: var(--red); }
  .card-contacts .address { color: var(--red); font-weight: 700; }

  .card-front .brand { left: 40px; top: 50px; gap: 10px; }
  .card-front .brand-square { width: 12px; height: 12px; }
  .card-front .brand-name { font-size: 20px; }
  .card-front .brand-name span + span { margin-top: 4px; }
  .about {
    position: absolute; left: 20px; right: 20px; top: 116px; text-align: center;
    font-family: "Lato", sans-serif; font-size: 5.6px; line-height: 8px; color: #444;
  }
  .about b { color: var(--red); }
</style>
</head>
<body>

<article class="sheet letterhead">
  <svg class="band band-top" viewBox="0 0 572 12" preserveAspectRatio="none" aria-hidden="true">
    <polygon points="0,0 180,0 170,12 0,12" fill="#3b3b3d"/>
    <polygon points="180,0 572,0 572,12 170,12" fill="#a3161c"/>
  </svg>

  <header class="brand">
    <span class="brand-square"></span>
    <div class="brand-name"><span>Maplerise</span><span>Trading</span></div>
  </header>

  <section class="letter-body">
    <p>Lorem ipsum dolor sit amet, consectetur adipiscing elit. Donec orci purus, luctus vitae dignissim eu, iaculis sed purus. Vivamus faucibus, ipsum nec aliquet viverra, leo mauris condimentum ligula, sit amet sagittis enim ligula quis arcu. Nam egestas tortor id nisi porttitor mattis. In tortor ante, ultricies in suscipit a, tempus non massa. Vivamus et auctor mi. Fusce vel massa nulla. Phasellus nec eros mauris, et scelerisque orci. Donec malesuada orci vitae nulla accumsan porta a id massa.</p>
    <p>Quisque accumsan iaculis magna sit amet fringilla. Maecenas consequat, magna eget tincidunt semper, odio nibh rutrum mi, id feugiat ante nisi eu risus. Vestibulum nunc orci, rhoncus a placerat in, ultricies in mi. Cras mattis varius eros, vel fringilla nisi suscipit eget. Quisque scelerisque sagittis nulla at porttitor. Mauris a justo et tellus interdum tristique. Sed id augue vitae urna euismod commodo aliquet a quam. Pellentesque arcu velit, cursus et malesuada ut, consequat et diam. Nullam erat sem, rhoncus id ullamcorper vitae, rhoncus et arcu. In ultricies ultricies nulla, fringilla nisi suscipit eget. Quisque scelerisque sagittis nulla at porttitor. Mauris a justo et tellus interdum tristique. Sed id augue vitae urna euismod commodo aliquet a quam. Pellentesque arcu velit, cursus et malesuada ut, consequat et diam. Nullam erat sem, rhoncus id ullamcorper vitae, rhoncus et arcu. In ultricies ultricies nulla,</p>
  </section>

  <div class="watermark" aria-hidden="true"></div>

  <div class="signature">
    <p class="name">Owen Hale</p>
    <p class="role">Co-Founder &amp; CEO</p>
  </div>

  <footer class="contacts">
    <dl><dt>Tel:</dt><dd>(555) 210-7390</dd><dt>Email:</dt><dd>(555) 210-7390</dd></dl>
    <dl><dt>Email:</dt><dd>sales@mapleriseinc.com</dd><dt>Web:</dt><dd>www.mapleriseinc.com</dd></dl>
    <p class="address">48 Birchwood Ave, Unit 9,<br>Oakridge</p>
  </footer>

  <svg class="band band-bottom" viewBox="0 0 572 12" preserveAspectRatio="none" aria-hidden="true">
    <polygon points="0,0 362,0 350,12 0,12" fill="#a3161c"/>
    <polygon points="362,0 572,0 572,12 350,12" fill="#3b3b3d"/>
  </svg>
</article>

<article class="card card-back">
  <header class="brand">
    <span class="brand-square"></span>
    <div class="brand-name"><span>Maplerise</span><span>Trading</span></div>
  </header>
  <div class="watermark" aria-hidden="true"></div>
  <div class="holder">
    <p class="name">LEAH MORROW</p>
    <p class="role">Founder</p>
  </div>
  <div class="card-contacts">
    <p><b>Tel:</b> (555) 210-7390<br><b>Email:</b> (555) 210-7390</p>
    <p><b>Email:</b> sales@mapleriseinc.com<br><b>Web:</b> www.mapleriseinc.com</p>
    <p class="address">48 Birchwood Ave, Unit 9,<br>Oakridge</p>
  </div>
  <svg class="band band-bottom" viewBox="0 0 272 6" preserveAspectRatio="none" aria-hidden="true">
    <polygon points="0,0 180,0 174,6 0,6" fill="#a3161c"/>
    <polygon points="180,0 272,0 272,6 174,6" fill="#3b3b3d"/>
  </svg>
</article>

<article class="card card-front">
  <header class="brand">
    <span class="brand-square"></span>
    <div class="brand-name"><span>Maplerise</span><span>Trading</span></div>
  </header>
  <p class="about"><b>Maplerise Trading Inc.</b> is one of the leading suppliers of<br>children's furniture, office furniture &amp; lighting fixtures.</p>
  <svg class="band band-bottom" viewBox="0 0 272 6" preserveAspectRatio="none" aria-hidden="true">
    <polygon points="0,0 180,0 174,6 0,6" fill="#a3161c"/>
    <polygon points="180,0 272,0 272,6 174,6" fill="#3b3b3d"/>
  </svg>
</article>

</body>
</html>
```